business card for a shoe shop

we would like a business card for a family owned shoe shop.
With this information included.
Darnell's Shoe Store
Family owned since 1947

then on other side
Darnell's Shoe Store
Footwear fitting specialist
Phone: 9187 2630
218 Quarry St, Fernleigh Downs 3187
(cnr. Hartwick Rd and Quarry St)
darnellshoes218@examplemail.com
if could incorporate the purple color on card i have attached.

```html
<!DOCTYPE html>
<html lang="en">
<head>
<meta charset="utf-8">
<title>Darnell's Shoe Store – Business Card</title>
<link rel="stylesheet" href="https://fonts.googleapis.com/css2?family=Montserrat:wght@400;500;600;700&display=swap">
<style>
  :root {
    --backdrop: #2b2b2e;
    --card-dark: #0b0b0c;
    --brand-purple: #5e4a9e;
    --brand-purple-light: #6d58b4;
    --text-light: #d9d9dc;
    --text-white: #ffffff;
  }
  * { box-sizing: border-box; margin: 0; padding: 0; }
  html, body {
    width: 1200px; height: 1200px; overflow: hidden;
    background: var(--backdrop);
    font-family: "Montserrat", Arial, sans-serif;
  }
  .stage {
    width: 1200px; height: 1200px;
    display: flex; align-items: center; justify-content: center; gap: 80px;
  }
  .card {
    width: 420px; height: 690px; border-radius: 26px;
    position: relative; display: flex; flex-direction: column; align-items: center;
    text-align: center;
  }
  .card--back { background: var(--card-dark); color: var(--text-light); padding: 62px 40px 0; }
  .card--front { background: var(--brand-purple); color: var(--text-white); justify-content: center; }

  .wordmark { display: flex; flex-direction: column; align-items: center; font-weight: 600; line-height: 1; }
  .wordmark__name { font-size: 50px; letter-spacing: 0.5px; }
  .wordmark__sub { font-size: 15px; letter-spacing: 6px; margin-top: 12px; }
  .card--back .wordmark { color: var(--brand-purple-light); }
  .card--front .wordmark { color: var(--text-white); }

  .business-name { margin-top: 150px; font-size: 23px; font-weight: 700; color: var(--brand-purple-light); }
  .tagline { margin-top: 6px; font-size: 15px; font-weight: 400; }

  .divider { width: 300px; height: 2px; background: var(--brand-purple); }
  .contact-rule { display: flex; align-items: center; gap: 10px; margin-top: 26px; }
  .contact-rule .divider { width: 100px; }
  .contact-icons { display: flex; gap: 6px; }
  .contact-icon { width: 24px; height: 24px; border-radius: 5px; background: var(--brand-purple); display: flex; align-items: center; justify-content: center; }

  .contact-list { list-style: none; margin-top: 16px; font-size: 15px; line-height: 1.75; }
  .address-rule { margin-top: 18px; }
  .address { margin-top: 18px; font-size: 15px; line-height: 1.5; font-style: normal; }

  .front-footer { position: absolute; bottom: 60px; left: 0; right: 0; display: flex; flex-direction: column; align-items: center; }
  .front-footer__mark { width: 30px; height: 3px; background: var(--text-white); margin-bottom: 18px; }
  .front-footer__text { font-size: 15px; font-weight: 400; }
</style>
</head>
<body>
<main class="stage">
  <section class="card card--back" aria-label="Card back with contact details">
    <div class="wordmark">
      <span class="wordmark__name">Darnell's</span>
      <span class="wordmark__sub">SHOE STORE</span>
    </div>
    <h1 class="business-name">Darnell's Shoe Store</h1>
    <p class="tagline">Footwear fitting specialist</p>
    <div class="contact-rule">
      <span class="divider"></span>
      <div class="contact-icons">
        <span class="contact-icon">
          <svg width="14" height="14" viewBox="0 0 24 24" aria-hidden="true"><path fill="#fff" d="M6.6 10.8a15.1 15.1 0 0 0 6.6 6.6l2.2-2.2c.3-.3.7-.4 1-.2 1.1.4 2.3.6 3.6.6.6 0 1 .4 1 1V20c0 .6-.4 1-1 1C10.6 21 3 13.4 3 4c0-.6.4-1 1-1h3.5c.6 0 1 .4 1 1 0 1.3.2 2.5.6 3.6.1.3 0 .7-.2 1z"/></svg>
        </span>
        <span class="contact-icon">
          <svg width="14" height="14" viewBox="0 0 24 24" aria-hidden="true"><rect x="3" y="5" width="18" height="14" rx="2" fill="#fff"/><path d="M3.5 6l8.5 7 8.5-7" fill="none" stroke="#5e4a9e" stroke-width="2"/></svg>
        </span>
        <span class="contact-icon">
          <svg width="14" height="14" viewBox="0 0 24 24" aria-hidden="true"><g fill="none" stroke="#fff" stroke-width="2"><circle cx="12" cy="12" r="9"/><ellipse cx="12" cy="12" rx="4" ry="9"/><path d="M3 12h18"/></g></svg>
        </span>
      </div>
      <span class="divider"></span>
    </div>
    <ul class="contact-list">
      <li>9187 2630</li>
      <li>darnellshoes218@examplemail.com</li>
      <li>www.darnellshoes.example</li>
    </ul>
    <span class="divider address-rule"></span>
    <address class="address">
      218 Quarry St, Fernleigh Downs 3187<br>
      (cnr. Hartwick Rd and Quarry St)
    </address>
  </section>

  <section class="card card--front" aria-label="Card front">
    <div class="wordmark">
      <span class="wordmark__name">Darnell's</span>
      <span class="wordmark__sub">SHOE STORE</span>
    </div>
    <div class="front-footer">
      <span class="front-footer__mark"></span>
      <p class="front-footer__text">Family owned since 1947</p>
    </div>
  </section>
</main>
</body>
</html>
```